Helping Seniors and their families start the discussion about driver safety, and explore options to preserve senior independence.
Target Market(s)
Seniors and their families
Industry/Entity Type
Non Profit
Number of Pages Required
4 page
Font styles to use
Sans Serif
Requirements
Must have
- Logo
- Application for Bright Pathways Registration

Nice to have
- Colorful, and designed for Senior Citizens and their Families

```html
<!DOCTYPE html>
<html lang="en">
<head>
<meta charset="utf-8">
<title>Bright Pathways</title>
<link rel="stylesheet" href="https://fonts.googleapis.com/css2?family=Open+Sans:wght@300;400;600;700&display=swap">
<style>
:root{
  --green:#1aa15a;
  --green-dark:#148a4b;
  --ink:#222;
  --muted:#555;
  --soft:#eef2f5;
  --tile:#e6e6e6;
  --tile-dark:#dcdcdc;
  --line:#cfd5d9;
  --white:#fff;
}
*{box-sizing:border-box;margin:0;padding:0}
html,body{width:1200px;height:3267px;overflow:hidden}
body{font-family:"Open Sans",Arial,sans-serif;color:var(--ink);background:var(--white);position:relative}
a{color:inherit;text-decoration:none}

/* header */
.site-header{position:absolute;top:0;left:0;width:1200px;height:109px;background:var(--white)}
.brand{position:absolute;left:87px;top:40px;white-space:nowrap}
.brand-name{color:var(--green);font-weight:700;font-size:20px;line-height:28px}
.main-nav{position:absolute;left:260px;top:0;height:109px;display:flex}
.main-nav a{display:flex;align-items:center;height:109px;padding:0 22px;font-size:14px;color:var(--ink)}
.main-nav a.active{color:var(--green);border-top:4px solid var(--green)}
.header-phone{position:absolute;left:767px;top:40px;font-size:18px;color:var(--ink);display:flex;align-items:center;gap:8px}
.header-phone strong{font-weight:600}
.social{display:flex;gap:6px}
.social span{width:30px;height:30px;border:2px solid var(--green);border-radius:50%;display:block}
.header-social{position:absolute;left:971px;top:39px}

/* hero */
.hero{position:absolute;top:109px;left:0;width:1200px;height:444px;background:linear-gradient(90deg,#2b2b2b 0%,#4a4a4a 45%,#a89a92 75%,#6a6260 100%)}
.hero-text{position:absolute;left:87px;top:158px;color:var(--white)}
.hero-text h1{font-weight:400;font-size:44px;line-height:50px}
.hero-text p{font-size:16px;line-height:20px;width:460px;margin-top:10px}
.btn-outline{display:inline-block;border:2px solid var(--white);color:var(--white);font-size:14px;padding:7px 24px;margin-top:26px}

/* feature strip */
.features{position:absolute;top:553px;left:0;width:1200px;height:301px;display:flex}
.feature{width:300px;height:301px;background:var(--tile);display:flex;flex-direction:column;align-items:center;padding-top:70px;text-align:center;font-size:15px;color:var(--ink)}
.feature:nth-child(4){background:var(--tile-dark)}
.feature.active{background:var(--green);color:var(--white)}
.feature.active .feature-label{text-decoration:underline}
.feature svg{width:90px;height:90px}
.feature-label{margin-top:24px;line-height:22px;width:190px}

/* intro */
.intro{position:absolute;top:854px;left:0;width:1200px;height:486px;background:var(--soft)}
.video{position:absolute;left:87px;top:63px;width:512px;height:348px;background:linear-gradient(135deg,#5a5f66 0%,#8d9298 50%,#3d4046 100%)}
.play{position:absolute;left:226px;top:144px;width:60px;height:60px;border:3px solid var(--white);border-radius:50%}
.play::after{content:"";position:absolute;left:22px;top:15px;border-left:20px solid var(--white);border-top:12px solid transparent;border-bottom:12px solid transparent}
.intro-text{position:absolute;left:647px;top:62px;width:440px}
.intro-text h2{font-weight:600;font-size:26px;padding-bottom:12px;border-bottom:1px solid var(--line);width:290px}
.intro-lead{font-weight:300;font-size:21px;line-height:28px;color:var(--muted);margin-top:22px}
.intro-body{font-size:13px;line-height:19px;color:var(--muted);margin-top:18px}
.btn-green{position:absolute;left:647px;top:374px;width:155px;height:37px;background:var(--green);color:var(--white);font-size:14px;display:flex;align-items:center;justify-content:center;gap:10px}

/* topics */
.topics{position:absolute;top:1340px;left:0;width:1200px;height:398px;display:flex}
.topic{position:relative;width:400px;height:398px;color:var(--white);text-align:center}
.topic-vision{background:linear-gradient(180deg,#6f7f92 0%,#9aa3a6 45%,#2c2a28 100%)}
.topic-hearing{background:radial-gradient(circle at 50% 40%,#a3707a 0%,#5a3646 55%,#2f1d27 100%)}
.topic-motor{background:linear-gradient(135deg,#8b8c88 0%,#b7b3aa 50%,#5c5b57 100%)}
.topic h3{font-weight:400;font-size:24px}
.topic p{font-size:13px;line-height:17px;width:300px;margin:6px auto 0}
.topic-caption{position:absolute;left:0;width:400px}
.topic-vision .topic-caption{top:272px}
.topic-hearing .topic-caption{top:198px}
.topic-motor .topic-caption{top:272px}
.btn-small{display:inline-flex;gap:10px;border:2px solid var(--white);font-size:13px;padding:6px 22px;margin-top:22px}

/* assess */
.assess{position:absolute;top:1738px;left:0;width:1200px;height:505px;background:var(--soft)}
.assess h2{position:absolute;top:68px;width:1200px;text-align:center;font-weight:600;font-size:31px}
.card{position:absolute;top:170px;width:501px;height:259px;border:1px dashed #b9c0c5}
.card-simple{left:87px}
.card-pro{left:612px}
.card-icon{position:absolute;left:44px;top:-26px;width:56px;height:60px;background:var(--soft)}
.card h3{position:absolute;left:44px;top:60px;font-weight:400;font-size:20px}
.card p{position:absolute;left:44px;top:100px;width:420px;font-size:13px;line-height:19px;color:var(--muted)}
.card-btn{position:absolute;left:44px;top:188px;height:37px;padding:0 18px;border:2px solid var(--green);font-size:13px;display:flex;align-items:center;gap:8px;background:var(--white)}

/* maintain */
.maintain{position:absolute;top:2243px;left:0;width:1200px;height:277px;background:linear-gradient(180deg,#4d4c4a 0%,#2b2a29 55%,#444 100%);color:var(--white);text-align:center}
.maintain h2{margin-top:70px;font-weight:600;font-size:28px}
.maintain p{font-size:15px;line-height:20px;width:840px;margin:8px auto 0}
.maintain .btn-small{margin-top:26px}

/* map */
.map{position:absolute;top:2520px;left:0;width:1200px;height:414px;background:linear-gradient(90deg,#e4e4e4 0%,#ececec 60%,#e7e7e7 100%)}
.map-pin{position:absolute;left:589px;top:170px}

/* footer */
.site-footer{position:absolute;top:2934px;left:0;width:1200px;height:333px;background:var(--soft)}
.footer-brand{position:absolute;left:87px;top:76px;white-space:nowrap}
.footer-contact{position:absolute;left:322px;top:74px;font-size:14px;line-height:20px;color:var(--muted)}
.footer-contact .call{font-size:20px;color:var(--ink);margin-bottom:4px}
.footer-contact .fax{font-size:12px}
.footer-contact .addr-label{margin-top:20px}
.footer-links{position:absolute;left:675px;top:74px;font-size:13px;line-height:20px;color:var(--muted)}
.footer-links h4,.newsletter h4{font-weight:600;font-size:14px;color:var(--ink);margin-bottom:4px}
.footer-links a{display:block}
.newsletter{position:absolute;left:849px;top:74px;width:264px}
.newsletter-field{margin-top:12px;height:36px;background:var(--white);border:1px solid var(--line);display:flex;align-items:center;justify-content:space-between;padding:0 12px;font-size:12px;font-style:italic;color:#888}
.newsletter .social{margin-top:18px}
.newsletter .social span:first-child{background:var(--green)}
.footer-bottom{position:absolute;left:87px;top:261px;width:1026px;border-top:1px solid var(--line);padding-top:18px;font-size:12px;color:var(--muted);display:flex;justify-content:space-between}
.to-top{width:0;height:0;border-left:11px solid transparent;border-right:11px solid transparent;border-bottom:18px solid var(--green)}
</style>
</head>
<body>

<header class="site-header">
  <a class="brand" href="#"><span class="brand-name">Bright Pathways</span></a>
  <nav class="main-nav">
    <a class="active" href="#">Who We Are?</a>
    <a href="#">Why Us?</a>
    <a href="#">Blog</a>
    <a href="#">Contact Us</a>
  </nav>
  <div class="header-phone">Call
    <svg width="16" height="18" viewBox="0 0 16 18"><rect x="2" y="1" width="11" height="16" rx="2" fill="var(--green)"/><rect x="4" y="3" width="7" height="10" fill="#fff"/></svg>
    <strong>404-555-0172</strong></div>
  <div class="social header-social" aria-label="Social links"><span></span><span></span><span></span><span></span></div>
</header>

<section class="hero" role="img" aria-label="Smiling senior woman at the wheel of a car giving a thumbs up">
  <div class="hero-text">
    <h1>Bright Pathways</h1>
    <p>Empowering Seniors with Independence and caregivers with peace of mind</p>
    <a class="btn-outline" href="#">Explore More</a>
  </div>
</section>

<section class="features">
  <a class="feature" href="#">
    <svg viewBox="0 0 90 90"><path d="M45 12a33 33 0 1 1-30 19" fill="none" stroke="var(--green)" stroke-width="8"/><path d="M45 28v20h16" fill="none" stroke="var(--green)" stroke-width="7"/><path d="M4 26l16-4 2 16z" fill="var(--green)"/></svg>
    <span class="feature-label">Renewing Your Driver's License</span>
  </a>
  <a class="feature active" href="#">
    <svg viewBox="0 0 90 90"><path d="M5 80L85 40v40z" fill="#fff"/><rect x="30" y="14" width="40" height="30" rx="4" fill="none" stroke="#fff" stroke-width="5" transform="rotate(-20 50 30)"/><circle cx="36" cy="52" r="6" fill="#fff"/><circle cx="68" cy="40" r="6" fill="#fff"/></svg>
    <span class="feature-label">Assess and Maintain Your Driving Skills</span>
  </a>
  <a class="feature" href="#">
    <svg viewBox="0 0 90 90"><circle cx="28" cy="28" r="16" fill="var(--green)"/><circle cx="28" cy="28" r="6" fill="var(--tile)"/><circle cx="62" cy="28" r="16" fill="var(--green)"/><path d="M58 36c0-12 10-14 10-6" fill="none" stroke="var(--tile)" stroke-width="3"/><circle cx="45" cy="66" r="17" fill="var(--green)"/><rect x="40" y="56" width="10" height="18" rx="4" fill="var(--tile)"/></svg>
    <span class="feature-label">How Aging Can Affect Your Driving</span>
  </a>
  <a class="feature" href="#">
    <svg viewBox="0 0 90 90"><rect x="8" y="22" width="74" height="56" rx="6" fill="var(--green)"/><rect x="30" y="10" width="30" height="14" rx="3" fill="none" stroke="var(--green)" stroke-width="5"/><path d="M45 36v28M31 50h28" stroke="#fff" stroke-width="9"/></svg>
    <span class="feature-label">Medications and Driving</span>
  </a>
</section>

<section class="intro">
  <div class="video" role="img" aria-label="Video still of a senior man smiling from the driver's seat"><span class="play"></span></div>
  <div class="intro-text">
    <h2>Seniors Driving</h2>
    <p class="intro-lead">Helping Seniors and their families start the discussion about driver safety, and explore options to preserve senior independence.</p>
    <p class="intro-body">The fact is that our population is aging and while more experience is a good thing, so is awareness that some age-related changes are inevitable. Those changes don't have to mean the end of a driving life.</p>
  </div>
  <a class="btn-green" href="#">Discover More <span>+</span></a>
</section>

<section class="topics">
  <div class="topic topic-vision" role="img" aria-label="Driver's hands on the wheel facing an open road under a dramatic sky">
    <div class="topic-caption"><h3>Vision</h3><p>Over the years, our pupils get smaller and can affect our ability to drive safely.</p></div>
  </div>
  <div class="topic topic-hearing" role="img" aria-label="Close-up of a human ear">
    <div class="topic-caption"><h3>Hearing</h3><p>Hearing loss can affect our ability our ability to react to our surroundings.</p><a class="btn-small" href="#">Learn More <span>+</span></a></div>
  </div>
  <div class="topic topic-motor" role="img" aria-label="Senior driver taking a lesson with an instructor in the passenger seat">
    <div class="topic-caption"><h3>Motor Skills</h3><p>Diminishing motor skills can affect reaction time.</p></div>
  </div>
</section>

<section class="assess">
  <h2>Assess Your Driving Skills</h2>
  <article class="card card-simple">
    <svg class="card-icon" viewBox="0 0 56 60"><rect x="10" y="4" width="36" height="48" fill="none" stroke="#e0442c" stroke-width="3"/><path d="M18 38c6-14 10-22 10-14s10 12 12 10" fill="none" stroke="#e0442c" stroke-width="3"/></svg>
    <h3>Simple Driving Assessment</h3>
    <p>In 10-15 minutes, drivers can answer questions a worksheet that will help to evaluate whether they need to take steps to improve their driving skills, and to pinpoint specific areas for improvement.</p>
    <a class="card-btn" href="#"><svg width="12" height="14" viewBox="0 0 12 14"><rect x="1" y="1" width="10" height="12" fill="none" stroke="#333" stroke-width="1.5"/></svg>View Test (PDF)</a>
  </article>
  <article class="card card-pro">
    <svg class="card-icon" viewBox="0 0 56 60"><rect x="10" y="6" width="36" height="48" rx="3" fill="none" stroke="#333" stroke-width="3"/><rect x="20" y="2" width="16" height="8" fill="#333"/><path d="M18 26l6 6 12-12" fill="none" stroke="#e0442c" stroke-width="3"/><path d="M18 42h20" stroke="#333" stroke-width="3"/></svg>
    <h3>Professional Driving Assessment</h3>
    <p>Have you have noticed that some of your skills needed for safe driving are not as strong as they used to be?</p>
    <a class="card-btn" href="#"><svg width="12" height="12" viewBox="0 0 12 12"><path d="M2 1l3 0 1 3-2 1c1 2 2 3 3 3l1-2 3 1v3c-6 0-10-4-10-9z" fill="#333"/></svg>Contact Us</a>
  </article>
</section>

<section class="maintain" role="img" aria-label="Hands on a steering wheel inside a car">
  <h2>Maintain Your Driving Skills</h2>
  <p>Bright Pathways has gathered information on ways to maintain driving skills, and although the information is intended for seniors, much of it would be helpful for all drivers.</p>
  <a class="btn-small" href="#">Find Out How <span>+</span></a>
</section>

<section class="map" role="img" aria-label="Street map showing the office location">
  <svg class="map-pin" width="24" height="34" viewBox="0 0 24 34"><path d="M12 0a12 12 0 0 1 12 12c0 9-12 22-12 22S0 21 0 12A12 12 0 0 1 12 0z" fill="var(--green)"/><circle cx="12" cy="12" r="5" fill="#fff"/></svg>
</section>

<footer class="site-footer">
  <a class="footer-brand" href="#"><span class="brand-name">Bright Pathways</span></a>
  <div class="footer-contact">
    <p class="call">Call: 404-555-0172</p>
    <p>Ride Reservation: 770-555-0148</p>
    <p class="fax">Fax: 678-555-0199</p>
    <p class="addr-label">Address:</p>
    <p>120 Maple Grove Road Suite 210 Alderton,<br>Georgia 30000</p>
  </div>
  <nav class="footer-links">
    <h4>Quick Link</h4>
    <a href="#">Who We Are?</a><a href="#">Why Us?</a><a href="#">Blog</a><a href="#">Contact Us</a>
  </nav>
  <div class="newsletter">
    <h4>Newsletter</h4>
    <div class="newsletter-field">Enter your email ...<svg width="16" height="14" viewBox="0 0 16 14"><path d="M0 6l16-6-4 14-4-5z" fill="#333"/></svg></div>
    <div class="social"><span></span><span></span><span></span><span></span></div>
  </div>
  <div class="footer-bottom"><span>© 2017, Bright Pathways. All Rights Reserved.</span><span class="to-top"></span></div>
</footer>

</body>
</html>
```